Mobile App UI for Telecommunications/Hosting Company

We are about to convert our existing self-service Customer Portal into a mobile phone application and need an elegant and professional UI/UX design. Our company provides telecommunication (voice/mobile/data) and hosting services to medium-sized business. The primary purpose of the application is to view trouble tickets, alerts, orders, and performance charts. This application is available to customers only - not the general public.

Please provide a UI design suitable for display on iPhone/Android devices. The attached document includes a proposed screen flow. You are free to design your own screens to display the same information elegantly.
Updates

Please note that the design should be based on the wireframes in the Word document, not the screenshots.  The screenshots are just to show our existing web portal look & feel.

Also, just a few screens are required for initial submission (3 would be great).

Thanks,
Dermot.

Target Market(s)

IT Managers away from their desk and using a mobile phone application.
Adult males from technical background aged 30-50.
Customers of Brindlewood Networks have access to this application (not the general public). This is a self-service portal for customers only.

Industry/Entity Type

Business

Colors
0592cd
33a6d7
85cae6
cadf82
fde08a

Requirements
Must have
• Please look at the screenshots from our current Customer Portal site (part of the project brief). The mobile app does not have to look the same, but should follow a similar style.

Please check out our company web site at www.brindlewoodnetworks.example (this site is not the customer portal and has a different look at feel) to understand what Brindlewood Networks does.
Nice to have
• Sharing capabilities via email/SMS.
A nice background image to make it stand out
The colours selected below are a guide only as they are similar to the corporate colours
- The priority is something that works on a phone - a design extendable to tablets is a nice to have as our existing web site looks OK on a tablet..

```html
<!DOCTYPE html>
<html lang="en">
<head>
<meta charset="utf-8">
<title>BrindlewoodView – Log in</title>
<link rel="stylesheet" href="https://fonts.googleapis.com/css2?family=Roboto:wght@300;400;500&display=swap">
<style>
  :root {
    --page-white: #ffffff;
    --ink: #111111;
    --ink-soft: #555a60;
    --link-blue: #33a6d7;
    --field-white: #ffffff;
    --panel-frost: rgba(232, 236, 241, 0.82);
    --button-frost: rgba(222, 226, 231, 0.85);
    --button-edge: #3a3d42;
    --photo-sky: #7a9cbc;
    --photo-glass: #a9b7c2;
    --photo-wall: #3f4a55;
    --photo-dark: #2b2f35;
    --photo-floor: #c9ccca;
    --photo-floor-deep: #9fa4a6;
  }
  * { box-sizing: border-box; margin: 0; padding: 0; }
  html, body {
    width: 1200px;
    height: 2313px;
    overflow: hidden;
    background: var(--page-white);
    font-family: "Roboto", "Helvetica Neue", Arial, sans-serif;
    color: var(--ink);
  }
  .app-screen {
    position: relative;
    width: 1200px;
    height: 2313px;
    overflow: hidden;
  }
  .status-bar {
    position: absolute;
    top: 0; left: 0; right: 0;
    height: 90px;
    display: flex;
    align-items: center;
    justify-content: space-between;
    padding: 0 24px;
    font-size: 42px;
    font-weight: 500;
    background: var(--page-white);
  }
  .status-left, .status-right { display: flex; align-items: center; gap: 14px; width: 380px; }
  .status-right { justify-content: flex-end; }
  .title-bar {
    position: absolute;
    top: 90px; left: 0; right: 0;
    height: 170px;
    display: flex;
    align-items: center;
    justify-content: center;
    font-size: 56px;
    font-weight: 400;
    background: var(--page-white);
  }
  .lobby-photo {
    position: absolute;
    top: 260px; left: 0; right: 0; bottom: 0;
    background: linear-gradient(180deg, var(--photo-sky) 0%, var(--photo-glass) 30%, var(--photo-wall) 60%, var(--photo-dark) 75%, var(--photo-floor) 88%, var(--photo-floor-deep) 100%);
  }
  .login-panel {
    position: absolute;
    left: 101px;
    top: 671px;
    width: 1006px;
    height: 1211px;
    background: var(--panel-frost);
  }
  .brand-name {
    position: absolute;
    top: 132px;
    left: 0; right: 0;
    text-align: center;
    font-size: 62px;
    font-weight: 400;
    color: var(--ink);
  }
  .field {
    position: absolute;
    left: 83px;
    width: 843px;
    height: 130px;
    background: var(--field-white);
    display: flex;
    align-items: center;
    padding-left: 38px;
    font-size: 44px;
    color: var(--ink-soft);
  }
  .field-username { top: 430px; }
  .field-password { top: 614px; }
  .remember-link {
    position: absolute;
    top: 828px;
    left: 0; right: 0;
    text-align: center;
    font-size: 40px;
    color: var(--link-blue);
  }
  .login-button {
    position: absolute;
    top: 1014px;
    left: 83px;
    width: 843px;
    height: 119px;
    border: 3px solid var(--button-edge);
    background: var(--button-frost);
    display: flex;
    align-items: center;
    justify-content: center;
    font-size: 58px;
    color: var(--ink);
  }
</style>
</head>
<body>
  <main class="app-screen">
    <header class="status-bar">
      <div class="status-left">
        <svg width="100" height="24" viewBox="0 0 100 24" aria-hidden="true">
          <circle cx="10" cy="12" r="9" fill="#111"/>
          <circle cx="30" cy="12" r="9" fill="#111"/>
          <circle cx="50" cy="12" r="9" fill="#111"/>
          <circle cx="70" cy="12" r="8" fill="none" stroke="#111" stroke-width="2"/>
          <circle cx="90" cy="12" r="8" fill="none" stroke="#111" stroke-width="2"/>
        </svg>
        <span class="status-carrier">Nimbus</span>
        <svg width="44" height="34" viewBox="0 0 44 34" aria-hidden="true">
          <path d="M22 32 L16 25 A9 9 0 0 1 28 25 Z" fill="#111"/>
          <path d="M9 18 A19 19 0 0 1 35 18" fill="none" stroke="#111" stroke-width="5"/>
          <path d="M2 10 A29 29 0 0 1 42 10" fill="none" stroke="#111" stroke-width="5"/>
        </svg>
      </div>
      <span class="status-time">4:21 PM</span>
      <div class="status-right">
        <svg width="24" height="40" viewBox="0 0 24 40" aria-hidden="true">
          <path d="M3 11 L20 28 L11 36 L11 4 L20 12 L3 29" fill="none" stroke="#111" stroke-width="3" stroke-linejoin="round"/>
        </svg>
        <span class="status-battery-level">100%</span>
        <svg width="80" height="36" viewBox="0 0 80 36" aria-hidden="true">
          <rect x="2" y="3" width="68" height="30" rx="5" fill="none" stroke="#111" stroke-width="3"/>
          <rect x="7" y="8" width="58" height="20" rx="2" fill="#111"/>
          <rect x="72" y="12" width="6" height="12" rx="2" fill="#111"/>
        </svg>
      </div>
    </header>

    <div class="title-bar">BrindlewoodView</div>

    <div class="lobby-photo" role="img" aria-label="Photo of a bright office lobby with glass walls and black leather sofas"></div>

    <section class="login-panel">
      <div class="brand-name">Brindlewood Networks</div>
      <div class="field field-username">Username</div>
      <div class="field field-password">Password</div>
      <div class="remember-link">Remember my logon details</div>
      <div class="login-button">Log in</div>
    </section>
  </main>
</body>
</html>
```